Harbourne Dental Care

I need a nice business card design that is double sided. This is for a dental surgery. I have already had a logo designed and just need the business card put together.

It needs to be in a format such that I can make new business cards if new dentists begin working for me. Hence I need to be able to change the text in order to have new names written on new cards.

The front will have the following text:

Dr Farid Osman
B. Med. Sci. QMTI B.Dent. Alb. Uni

The logo will appear somewhere on the front. This is attached.

In addition will be the following writing that also needs to appear on the front of the card, perhaps at the bottom on the left side will be:

Shop 42, 210-238 Fernlow Street, North Sydney, NSW, 2060

and at the bottom on the right side will be:
(02) 5550 8137
e: info@harbournedentalcare.com.au
www.harbournedentalcare.com.au

On the back of the card will be a section for a map to be drawn (I have uploaded a picture) and also a section written as follows:

"Your next appointment is: (a line needs to be here to write date and time)"

Also I need two lines for two appointments to be written.

Thanks for your efforts!

```html
<!DOCTYPE html>
<html lang="en">
<head>
<meta charset="utf-8">
<title>Harbourne Dental Care – Business Card</title>
<link rel="stylesheet" href="https://fonts.googleapis.com/css2?family=Noto+Serif:wght@400;700&display=swap">
<style>
  :root {
    --navy: #2c4a9a;
    --navy-deep: #223d85;
    --sky: #3dbdf0;
    --sky-deep: #1b9ad8;
    --card: #f7f9fb;
    --map: #dcd5c6;
    --stage: #e7eaee;
    --white: #ffffff;
  }
  * { margin: 0; padding: 0; box-sizing: border-box; }
  html, body { width: 1200px; height: 665px; overflow: hidden; }
  body {
    background: var(--stage);
    font-family: "Noto Serif", Georgia, serif;
    position: relative;
  }
  .card {
    position: absolute;
    width: 540px;
    height: 309px;
    background: var(--card);
    overflow: hidden;
    box-shadow: 0 6px 18px rgba(20, 35, 70, 0.18);
  }
  .card-front { left: 40px; top: 320px; }
  .card-back { left: 620px; top: 40px; }
  .card-shapes { position: absolute; inset: 0; width: 100%; height: 100%; }

  .brand {
    position: absolute;
    display: flex;
    align-items: center;
    gap: 10px;
    color: var(--navy);
    font-weight: 700;
  }
  .brand-dot {
    width: 14px; height: 14px; border-radius: 50%;
    background: var(--navy);
    flex: none;
  }
  .brand-name { font-size: 22px; line-height: 1.15; letter-spacing: 0.5px; }
  .card-front .brand { left: 34px; top: 100px; }
  .card-back .brand { left: 60px; top: 36px; }
  .card-back .brand-name { font-size: 19px; }

  .dentist {
    position: absolute;
    right: 28px;
    top: 18px;
    text-align: center;
  }
  .dentist-name { color: var(--white); font-size: 29px; font-weight: 700; line-height: 1.1; }
  .dentist-degrees { color: var(--navy); font-size: 11px; font-weight: 700; margin-top: 4px; }

  .contacts {
    position: absolute;
    right: 18px;
    top: 200px;
    list-style: none;
    color: var(--white);
    font-size: 11.5px;
    font-weight: 700;
    text-align: right;
  }
  .contacts li { display: flex; justify-content: flex-end; align-items: center; gap: 8px; height: 21px; }
  .contacts svg { width: 14px; height: 14px; flex: none; }

  .address {
    position: absolute;
    left: 24px;
    bottom: 20px;
    display: flex;
    align-items: flex-start;
    gap: 8px;
    color: var(--navy);
    font-size: 13.5px;
    font-weight: 700;
    font-style: normal;
    line-height: 1.35;
  }
  .address svg { width: 14px; height: 20px; margin-top: 14px; flex: none; }

  .appointment { position: absolute; left: 60px; top: 126px; width: 215px; }
  .appointment-label { color: var(--navy); font-size: 12px; text-align: center; }
  .appointment-line { height: 1px; background: var(--navy); margin-top: 27px; }
</style>
</head>
<body>

  <section class="card card-front" aria-label="Business card front">
    <svg class="card-shapes" viewBox="0 0 540 309" aria-hidden="true">
      <defs>
        <linearGradient id="front-sky" x1="0" y1="0" x2="1" y2="1">
          <stop offset="0" stop-color="#4cc8f4"/>
          <stop offset="1" stop-color="#1b9ad8"/>
        </linearGradient>
      </defs>
      <path d="M262,0 C222,40 222,105 268,145 C298,172 272,212 252,238 C236,260 230,290 232,309 L540,309 L540,0 Z" fill="url(#front-sky)"/>
      <path d="M282,309 C276,262 300,224 345,222 C372,195 430,190 462,205 C500,192 525,196 540,202 L540,309 Z" fill="#2c4a9a"/>
      <path d="M350,309 C342,276 370,256 398,262 C416,244 450,246 462,262 C490,252 520,262 540,270 L540,309 Z" fill="#1b9ad8" opacity="0.55"/>
      <circle cx="400" cy="162" r="24" fill="#2c4a9a"/>
      <circle cx="240" cy="208" r="19" fill="#2c4a9a"/>
    </svg>

    <div class="brand">
      <span class="brand-dot"></span>
      <span class="brand-name">Harbourne<br>Dental Care</span>
    </div>

    <div class="dentist">
      <p class="dentist-name">Dr Farid Osman</p>
      <p class="dentist-degrees">B. Med. Sci. QMTI B.Dent. Alb. Uni</p>
    </div>

    <ul class="contacts">
      <li>(02) 5550 8137
        <svg viewBox="0 0 24 24" aria-hidden="true"><path fill="#fff" d="M6.6 10.8a15.1 15.1 0 0 0 6.6 6.6l2.2-2.2c.3-.3.7-.4 1-.2 1.1.4 2.3.6 3.6.6.6 0 1 .4 1 1V20c0 .6-.4 1-1 1A17 17 0 0 1 3 4c0-.6.4-1 1-1h3.5c.6 0 1 .4 1 1 0 1.3.2 2.5.6 3.6.1.3 0 .7-.2 1z"/></svg>
      </li>
      <li>info@harbournedentalcare.com.au
        <svg viewBox="0 0 24 24" aria-hidden="true"><rect x="2" y="5" width="20" height="14" rx="1.5" fill="none" stroke="#fff" stroke-width="2"/><path d="M2.5 6l9.5 7 9.5-7" fill="none" stroke="#fff" stroke-width="2"/></svg>
      </li>
      <li>www.harbournedentalcare.com.au
        <svg viewBox="0 0 24 24" aria-hidden="true"><circle cx="12" cy="12" r="9.5" fill="none" stroke="#fff" stroke-width="2"/><path d="M2.5 12h19M12 2.5c3 3 3 16 0 19M12 2.5c-3 3-3 16 0 19" fill="none" stroke="#fff" stroke-width="1.6"/></svg>
      </li>
    </ul>

    <address class="address">
      <svg viewBox="0 0 14 20" aria-hidden="true"><path d="M7 0a7 7 0 0 0-7 7c0 5 7 13 7 13s7-8 7-13a7 7 0 0 0-7-7z" fill="#2c4a9a"/><circle cx="7" cy="7" r="2.5" fill="#f7f9fb"/></svg>
      <span>Shop 42, 210-238 Fernlow Street,<br>North Sydney, NSW, 2060</span>
    </address>
  </section>

  <section class="card card-back" aria-label="Business card back">
    <svg class="card-shapes" viewBox="0 0 540 309" aria-hidden="true">
      <path d="M470,0 C450,30 470,62 505,70 C520,74 532,82 540,92 L540,0 Z" fill="#2c4a9a"/>
      <path d="M300,309 C300,262 350,232 400,240 C420,214 462,214 480,236 C505,240 525,256 540,270 L540,309 Z" fill="#2c4a9a"/>
      <path d="M470,160 C500,190 520,235 500,268 C488,290 462,284 460,262 C458,236 470,210 455,185 Z" fill="#1b9ad8"/>
      <circle cx="320" cy="190" r="20" fill="#2c4a9a"/>
      <circle cx="432" cy="104" r="98" fill="#3dbdf0"/>
      <circle cx="432" cy="104" r="91" fill="#dcd5c6" role="img" aria-label="Street map showing the surgery location"/>
    </svg>

    <div class="brand">
      <span class="brand-dot"></span>
      <span class="brand-name">Harbourne<br>Dental Care</span>
    </div>

    <div class="appointment">
      <p class="appointment-label">Your next appointment is on</p>
      <div class="appointment-line"></div>
      <div class="appointment-line"></div>
    </div>
  </section>

</body>
</html>
```